A wordpress website for the coolest Resort App

We have developed a mobile app - Zorbo and we want to develop a cool, neat and simple wordpress website for it.

I have attached the basics in a keynote/ ppt - but i need you to bring it more to life. plus there are additions:

FOr the number of pages, we will have:
1- Home: very similar to the one pager
2- How it works: Showing step by step on how the app works, and how it connects to the POS system of the restaurant etc with spanshots from the app
3- Benefit: Elaborating more on each of the benefits that is mentioned in the ONE PAGE document, with additional statistics, reference etc.. and embedded videos and animation
4- who we are page
5- In the press page: links to the articles where zorbo was mentioned
6- Get in touch page
7- FAQ
Updates

Target Market(s)

Resorts, hotels, beach and pool restaurant operators

Industry/Entity Type

Hospitality

Coding

Coded - Design and coding required

Font styles to use
Other font styles liked:
• I have attached the fonts i want to use: ROboto is the main font

Colors

Designer to choose colors to be used in the design.

Requirements
Must have
• Logo, icons for each benefit, you can also use the mood picture i attached or any other picture you recommend - maybe just something related to the app
• I also attached the Main colour, the orange and the blue is the accent one
• I attached the fonts, roboto is the main one
• there should also be a contact us:
• Email : info@zorboapp-mail.com
• Mobile: +971 5 23 47 90 18
• Address: Palm Quarter - Dubai - United Arab Emirates

```html
<!DOCTYPE html>
<html lang="en">
<head>
<meta charset="utf-8">
<title>Zorbo — Resort App</title>
<link href="https://fonts.googleapis.com/css2?family=Roboto:wght@300;400;500;700&family=Ubuntu:wght@300;400&display=swap" rel="stylesheet">
<style>
:root{
  --orange:#ff7845;
  --orange-dark:#f2602b;
  --blue:#2b9bd0;
  --blue-dark:#1e7fb0;
  --ink:#3a3a3a;
  --muted:#6d6d6d;
  --page:#efefef;
  --rule:#b9b9b9;
  --dark:#2f2f2f;
  --footer:#383838;
  --white:#ffffff;
}
*{box-sizing:border-box;margin:0;padding:0}
html,body{width:1200px;height:3930px;overflow:hidden}
body{position:relative;background:var(--page);font-family:'Roboto',sans-serif;color:var(--ink)}
.abs{position:absolute}
.topbar{left:0;top:0;width:1200px;height:26px;background:var(--dark)}
.header-bg{left:0;top:26px;width:1200px;height:180px}
.logo-box{left:79px;top:13px;width:222px;height:150px}
.logo-name{left:160px;top:50px;font:700 58px 'Roboto',sans-serif;color:var(--dark);letter-spacing:-1px}
.logo-dot{left:98px;top:66px;width:46px;height:46px;background:var(--orange)}
.social-top{top:40px;display:flex;gap:6px;left:790px}
.social-top span{width:22px;height:22px;border-radius:3px;display:block}
.search{left:890px;top:40px;width:230px;height:22px;background:var(--white);border:1px solid #999;font-size:13px;padding:3px 6px;color:#333}
.nav{top:104px;left:0;width:1200px}
.nav a{position:absolute;color:var(--white);text-decoration:none;font-size:19px;font-weight:400}
.nav a.active{border-bottom:2px solid var(--white);padding-bottom:6px}
.hero{left:79px;top:210px;width:1042px;height:576px;background:linear-gradient(180deg,#1d3c5c 0%,#2e5b74 35%,#7a5a3c 62%,#c08540 75%,#1d3a4d 100%);box-shadow:0 2px 6px rgba(0,0,0,.35)}
.hero-title{left:79px;top:396px;width:1042px;text-align:center;color:var(--white);font:400 46px 'Roboto',sans-serif;text-transform:uppercase;letter-spacing:.5px}
.hero-sub{left:290px;top:462px;width:620px;text-align:center;color:var(--white);font-size:16px;line-height:23px}
.btn{background:var(--orange);color:var(--white);text-transform:uppercase;font-size:19px;display:flex;align-items:center;justify-content:center;border-radius:30px}
.hero-btn{left:496px;top:535px;width:208px;height:50px}
.arrow-o{left:899px;top:584px;width:84px;height:40px;background:var(--orange)}
.arrow-b{left:899px;top:634px;width:84px;height:40px;background:var(--blue)}
.dots{left:541px;top:805px;display:flex;gap:10px}
.dots span{width:20px;height:20px;border-radius:50%;background:#cfcfcf;border:2px solid #e5e5e5}
.dots span.on{background:var(--orange)}
.section-title{width:1200px;left:0;text-align:center;font:400 40px 'Ubuntu',sans-serif;color:var(--ink)}
.section-title em{font-style:normal;color:var(--orange)}
.title-mark{left:560px;width:80px;height:14px}
.body-text{font-size:13.5px;line-height:22px;color:var(--muted)}
.welcome-text{left:190px;top:962px;width:820px;text-align:center}
.read-more{left:495px;top:1106px;width:210px;height:56px;font-size:18px}
.rule{left:79px;width:1042px;border-top:2px dashed var(--rule)}
.benefit-panel{left:79px;top:1276px;width:1042px;height:540px}
.benefit-h{font-size:24px;color:var(--blue-dark);font-weight:400}
.benefit-p{font-size:13.5px;line-height:22px;color:var(--muted);width:290px}
.right{text-align:right}
.icon-sq{width:106px;height:106px;background:var(--blue);border:4px solid #d9eef8}
.quote-text{left:190px;top:2013px;width:820px;text-align:center;font-size:14px;line-height:24px;color:var(--muted)}
.quote-mark{font:700 60px 'Roboto',sans-serif;color:var(--orange);line-height:1}
.testi-name{left:0;width:1200px;top:2124px;text-align:center;font-size:19px;color:var(--blue)}
.photo{left:558px;top:2180px;width:84px;height:84px;border:3px solid #ddd;background:linear-gradient(180deg,#dfe4ea,#b7c1cc)}
.sq{width:12px;height:12px;background:var(--blue)}
.step-title{font-size:24px;color:var(--orange);text-transform:uppercase;text-align:center}
.step-text{font-size:13.5px;line-height:21px;color:var(--muted);text-align:center;width:200px}
.step-text b{color:#333;text-decoration:underline;font-weight:700}
.news-img{top:3228px;width:333px;height:170px}
.date{top:3406px;width:58px;height:78px;background:var(--blue);color:var(--white);text-align:center;padding-top:6px}
.date b{display:block;font-size:28px;font-weight:500;line-height:30px;border-bottom:1px solid var(--white);margin:0 6px}
.date span{font-size:24px}
.news-h{top:3404px;width:262px;font-size:16px;font-weight:700;line-height:22px;color:#222}
.news-p{top:3452px;width:262px;font-size:14px;line-height:22px;color:var(--muted)}
.footer{left:0;top:3571px;width:1200px;height:359px;background:var(--footer)}
.f-title{top:3620px;font-size:19px;font-weight:700;color:var(--white)}
.field{border:1px solid #8a8a8a;color:#ccc;font-size:14px;display:flex;align-items:center;padding-left:12px;gap:10px;background:#444}
.field i{display:block;width:12px;height:12px;background:#ddd;border-radius:2px}
.submit{left:317px;top:3773px;width:260px;height:42px;background:var(--orange);color:var(--white);font-size:22px;font-weight:500;display:flex;align-items:center;justify-content:center}
.links{left:608px;top:3660px;list-style:none;color:#ddd;font-size:14px;line-height:29px}
.contact-line{color:#ddd;font-size:15px;line-height:26px}
.c-icon{width:38px;height:38px;border:2px solid #ddd;border-radius:50%}
.f-rule{left:79px;top:3865px;width:1042px;border-top:1px solid #666}
.copy{left:79px;top:3886px;font-size:14px;color:#ddd}
.f-social{width:38px;height:38px;border-radius:50%;background:#555}
</style>
</head>
<body>

<div class="abs topbar"></div>
<svg class="abs header-bg" viewBox="0 0 1200 180" width="1200" height="180" aria-hidden="true">
  <defs><linearGradient id="hg" x1="0" y1="0" x2="1" y2="0"><stop offset="0" stop-color="#ff6f3c"/><stop offset="1" stop-color="#ff8a55"/></linearGradient></defs>
  <path d="M0 0H1200V200C1040 170 900 150 780 150C600 150 420 138 0 130Z" fill="url(#hg)"/>
  <path d="M780 150C900 150 1040 165 1200 195" fill="none" stroke="#ff9a6c" stroke-width="3"/>
</svg>

<svg class="abs logo-box" viewBox="0 0 222 150" width="222" height="150" aria-hidden="true">
  <path d="M0 0H222V128L111 150L0 128Z" fill="#fff"/>
</svg>
<div class="abs logo-dot"></div>
<div class="abs logo-name">zorbo</div>

<div class="abs social-top"><span style="background:#3b63b0"></span><span style="background:#d9483b"></span><span style="background:#2fa5e0"></span></div>
<div class="abs search">Search Here</div>

<nav class="abs nav">
  <a class="active" style="left:414px">Home</a>
  <a style="left:516px">How it works</a>
  <a style="left:676px">Benefit</a>
  <a style="left:796px">who we are</a>
  <a style="left:954px">Faq</a>
  <a style="left:1037px">Contact</a>
</nav>

<div class="abs hero" role="img" aria-label="Resort pool deck at dusk with a lit wooden jetty and palm trees"></div>
<div class="abs hero-title">Make your holiday trip here</div>
<div class="abs hero-sub">Lorem Ipsum is simply dummy text of the printing and typesetting industry. Lorem Ipsum has been the industry's standard dummy text ever since the 1500s</div>
<div class="abs btn hero-btn">Contact us</div>
<div class="abs arrow-o"></div>
<div class="abs arrow-b"></div>
<div class="abs dots"><span class="on"></span><span></span><span></span><span></span></div>

<h2 class="abs section-title" style="top:872px">Welcome to <em>Zorbo</em></h2>
<svg class="abs title-mark" style="top:930px" viewBox="0 0 80 14" aria-hidden="true"><line x1="0" y1="7" x2="80" y2="7" stroke="#ccc"/><path d="M32 1L48 7L32 13L36 7Z" fill="#ff7845"/></svg>
<p class="abs body-text welcome-text">Lorem Ipsum is simply dummy text of the printing and typesetting industry. Lorem Ipsum has been the industry's standard dummy text ever since the 1500s, when an unknown printer took a galley of type and scrambled it to make a type specimen book. It has survived not only five centuries, but also the leap into electronic typesetting, remaining essentially unchanged. It was popularised in the 1960s with the release of Letraset sheets containing Lorem Ipsum passages, and more recently with desktop publishing software like Aldus PageMaker including versions of Lorem Ipsum.</p>
<div class="abs btn read-more">Read more</div>

<div class="abs rule" style="top:1218px"></div>

<svg class="abs benefit-panel" viewBox="0 0 1042 540" width="1042" height="540" aria-hidden="true">
  <path d="M40 0H1002L1042 270L1002 540H40L0 270Z" fill="#fff" stroke="#d8d8d8" stroke-width="2"/>
  <rect x="25" y="306" width="300" height="12" fill="#e6e6e6"/>
  <rect x="717" y="306" width="300" height="12" fill="#e6e6e6"/>
  <rect x="411" y="202" width="218" height="220" fill="none" stroke="#333" stroke-width="5"/>
  <circle cx="520" cy="312" r="48" fill="#fff"/>
  <circle cx="520" cy="312" r="36" fill="#ff7845"/>
</svg>
<h2 class="abs section-title" style="top:1325px">Zorbo <em>Benefit</em></h2>
<svg class="abs title-mark" style="top:1380px" viewBox="0 0 80 14" aria-hidden="true"><line x1="0" y1="7" x2="80" y2="7" stroke="#ccc"/><path d="M32 1L48 7L32 13L36 7Z" fill="#ff7845"/></svg>

<div class="abs icon-sq" style="left:437px;top:1425px"></div>
<div class="abs icon-sq" style="left:655px;top:1425px"></div>
<div class="abs icon-sq" style="left:437px;top:1645px"></div>
<div class="abs icon-sq" style="left:655px;top:1645px"></div>
<svg class="abs" style="left:437px;top:1425px" width="106" height="106" viewBox="0 0 106 106" aria-hidden="true"><rect x="34" y="24" width="38" height="58" rx="3" fill="none" stroke="#fff" stroke-width="4"/><line x1="42" y1="40" x2="64" y2="40" stroke="#fff" stroke-width="3"/><line x1="42" y1="52" x2="64" y2="52" stroke="#fff" stroke-width="3"/><line x1="42" y1="64" x2="58" y2="64" stroke="#fff" stroke-width="3"/></svg>
<svg class="abs" style="left:655px;top:1425px" width="106" height="106" viewBox="0 0 106 106" aria-hidden="true"><rect x="30" y="22" width="36" height="62" rx="5" fill="none" stroke="#fff" stroke-width="4"/><path d="M56 56L80 44L78 68Z" fill="#fff"/></svg>
<svg class="abs" style="left:437px;top:1645px" width="106" height="106" viewBox="0 0 106 106" aria-hidden="true"><circle cx="53" cy="56" r="26" fill="none" stroke="#fff" stroke-width="4"/><path d="M53 42V57L63 63" fill="none" stroke="#fff" stroke-width="4"/><circle cx="32" cy="30" r="7" fill="#fff"/><circle cx="74" cy="30" r="7" fill="#fff"/></svg>
<svg class="abs" style="left:655px;top:1645px" width="106" height="106" viewBox="0 0 106 106" aria-hidden="true"><rect x="26" y="24" width="40" height="58" rx="4" fill="none" stroke="#fff" stroke-width="4"/><rect x="46" y="52" width="36" height="24" rx="3" fill="#fff"/><line x1="50" y1="60" x2="78" y2="60" stroke="#2b9bd0" stroke-width="3"/></svg>

<div class="abs benefit-h right" style="left:114px;top:1422px;width:300px">Menu</div>
<p class="abs benefit-p right" style="left:124px;top:1456px">Lorem Ipsum is simply dummy text of the printing and typesetting industry. Lorem Ipsum has been the industry's standard...[+]</p>
<div class="abs benefit-h" style="left:783px;top:1422px">Customization</div>
<p class="abs benefit-p" style="left:783px;top:1456px">Lorem Ipsum is simply dummy text of the printing and typesetting industry. Lorem Ipsum has been the industry's standard...[+]</p>
<div class="abs benefit-h right" style="left:114px;top:1642px;width:300px">Speed</div>
<p class="abs benefit-p right" style="left:124px;top:1676px">Lorem Ipsum is simply dummy text of the printing and typesetting industry. Lorem Ipsum has been the industry's standard...[+]</p>
<div class="abs benefit-h" style="left:783px;top:1642px">Fast Checkout</div>
<p class="abs benefit-p" style="left:783px;top:1676px">Lorem Ipsum is simply dummy text of the printing and typesetting industry. Lorem Ipsum has been the industry's standard...[+]</p>

<div class="abs rule" style="top:1873px"></div>

<h2 class="abs section-title" style="top:1914px">Clients <em>Testimonials</em></h2>
<svg class="abs title-mark" style="top:1970px" viewBox="0 0 80 14" aria-hidden="true"><line x1="0" y1="7" x2="80" y2="7" stroke="#ccc"/><path d="M32 1L48 7L32 13L36 7Z" fill="#ff7845"/></svg>
<div class="abs quote-mark" style="left:158px;top:2000px">&ldquo;</div>
<p class="abs quote-text">Lorem Ipsum is simply dummy text of the printing and typesetting industry. Lorem Ipsum has been the industry's standard dummy text ever since the 1500s, when an unknown printer took a galley of type and scrambled it to make a type specimen book. It has survived not only five centuries.</p>
<div class="abs quote-mark" style="left:752px;top:2058px">&rdquo;</div>
<div class="abs testi-name">- Mara Velden.</div>
<div class="abs photo" role="img" aria-label="Portrait of the client giving the testimonial"></div>
<div class="abs sq" style="left:512px;top:2250px"></div><div class="abs sq" style="left:530px;top:2250px"></div>
<div class="abs sq" style="left:658px;top:2250px"></div><div class="abs sq" style="left:676px;top:2250px"></div>

<div class="abs rule" style="top:2324px"></div>

<h2 class="abs section-title" style="top:2372px">How it <em>Work</em></h2>
<svg class="abs title-mark" style="top:2428px" viewBox="0 0 80 14" aria-hidden="true"><line x1="0" y1="7" x2="80" y2="7" stroke="#ccc"/><path d="M32 1L48 7L32 13L36 7Z" fill="#ff7845"/></svg>

<svg class="abs" style="left:0;top:2470px" width="1200" height="480" viewBox="0 2470 1200 480" aria-hidden="true">
  <path d="M157 2712C230 2800 290 2843 354 2843C430 2843 500 2705 580 2705C680 2705 740 2594 833 2594C930 2594 980 2700 1040 2756" fill="none" stroke="#ff7845" stroke-width="30" stroke-linecap="round"/>
  <g fill="#fff" stroke="#2b9bd0" stroke-width="12">
    <circle cx="157" cy="2712" r="88"/>
    <circle cx="354" cy="2843" r="70"/>
    <circle cx="580" cy="2705" r="72"/>
    <circle cx="833" cy="2594" r="78"/>
    <circle cx="1040" cy="2756" r="78"/>
  </g>
  <g fill="none" stroke="#222" stroke-width="6" stroke-linejoin="round">
    <g transform="translate(157 2712)">
      <path d="M0 24C-17 0-25-14-25-26A25 25 0 0 1 25-26C25-14 17 0 0 24Z"/>
      <circle cx="0" cy="-26" r="8"/>
      <path d="M-37 32H37L46 50H-46Z"/>
    </g>
    <g transform="translate(354 2843)">
      <rect x="-30" y="-26" width="60" height="50" rx="4"/>
      <line x1="-30" y1="-14" x2="30" y2="-14"/>
      <path d="M-10 14L10-4M10-4H-4M10-4V10"/>
    </g>
    <g transform="translate(580 2705)">
      <rect x="-40" y="-26" width="80" height="52" rx="5"/>
      <rect x="-26" y="-16" width="22" height="32"/>
    </g>
    <g transform="translate(833 2594)">
      <path d="M-36 18H36M-30 14A30 30 0 0 1 30 14M0-16V-22"/>
    </g>
    <g transform="translate(1040 2756)">
      <rect x="-40" y="-24" width="80" height="48" rx="4"/>
      <circle cx="0" cy="0" r="13"/>
    </g>
  </g>
  <g fill="#222">
    <circle cx="157" cy="2600" r="17"/><circle cx="354" cy="2748" r="17"/><circle cx="580" cy="2612" r="17"/><circle cx="833" cy="2494" r="17"/><circle cx="1032" cy="2655" r="17"/>
  </g>
  <g fill="#fff" font-family="Roboto, sans-serif" font-size="18" font-weight="700" text-anchor="middle">
    <text x="157" y="2606">1</text><text x="354" y="2754">2</text><text x="580" y="2618">3</text><text x="833" y="2500">4</text><text x="1032" y="2661">5</text>
  </g>
</svg>

<div class="abs step-title" style="left:37px;top:2810px;width:200px">Locate</div>
<p class="abs step-text" style="left:49px;top:2850px">Lorem Ipsum is simply dummy text of the printing and typesetting industry. Lorem Ipsum has been the industry's standard dummy text ever since the 1500s.<b>READ MORE</b></p>
<p class="abs step-text" style="left:262px;top:2530px">Lorem Ipsum is simply dummy text of the printing and typesetting industry. Lorem Ipsum has been the industry's standard dummy text ever since the 1500s.<b>READ MORE</b></p>
<div class="abs step-title" style="left:262px;top:2680px;width:200px">Browse</div>
<div class="abs step-title" style="left:503px;top:2840px;width:200px">Order</div>
<p class="abs step-text" style="left:503px;top:2876px">Lorem Ipsum is simply dummy text of the printing and typesetting industry. Lorem Ipsum has been the industry's standard dummy text ever since the 1500s.<b>READ MORE</b></p>
<div class="abs step-title" style="left:733px;top:2734px;width:200px">Help</div>
<p class="abs step-text" style="left:740px;top:2770px">Lorem Ipsum is simply dummy text of the printing and typesetting industry. Lorem Ipsum has been the industry's standard dummy text ever since the 1500s.<b>READ MORE</b></p>
<p class="abs step-text" style="left:925px;top:2455px;width:195px">Lorem Ipsum is simply dummy text of the printing and typesetting industry. Lorem Ipsum has been the industry's standard dummy text ever since the 1500s.<b>READ MORE</b></p>
<div class="abs step-title" style="left:930px;top:2607px;width:200px">Pay</div>

<div class="abs rule" style="top:3060px"></div>

<h2 class="abs section-title" style="top:3118px">Latest <em>News</em></h2>
<svg class="abs title-mark" style="top:3174px" viewBox="0 0 80 14" aria-hidden="true"><line x1="0" y1="7" x2="80" y2="7" stroke="#ccc"/><path d="M32 1L48 7L32 13L36 7Z" fill="#ff7845"/></svg>

<div class="abs news-img" style="left:79px;background:linear-gradient(135deg,#3fb8e6,#1f8fc4 60%,#f2f2f2)" role="img" aria-label="Guest in a sun hat relaxing at a resort pool"></div>
<div class="abs news-img" style="left:432px;background:linear-gradient(135deg,#3a3f48,#6a7480 55%,#2b5c8a)" role="img" aria-label="Hand paying with a phone at a card terminal"></div>
<div class="abs news-img" style="left:789px;background:linear-gradient(135deg,#7fc4e8,#4a8fb8 45%,#b07848)" role="img" aria-label="Coffee cup on a poolside table"></div>

<div class="abs date" style="left:79px"><b>05</b><span>Sep</span></div>
<div class="abs news-h" style="left:150px">Lorem ipsum is simply dummy text of the printing</div>
<div class="abs news-p" style="left:150px">Lorem Ipsum is simply dummy text of the printing and typesetting industry.</div>
<div class="abs date" style="left:432px"><b>05</b><span>Sep</span></div>
<div class="abs news-h" style="left:503px">Lorem ipsum is simply dummy text of the printing</div>
<div class="abs news-p" style="left:503px">Lorem Ipsum is simply dummy text of the printing and typesetting industry.</div>
<div class="abs date" style="left:789px"><b>05</b><span>Sep</span></div>
<div class="abs news-h" style="left:860px">Lorem ipsum is simply dummy text of the printing</div>
<div class="abs news-p" style="left:860px">Lorem Ipsum is simply dummy text of the printing and typesetting industry.</div>

<footer class="abs footer"></footer>
<div class="abs f-title" style="left:81px">Keep In Touch</div>
<div class="abs field" style="left:81px;top:3660px;width:226px;height:42px"><i></i>Your Name:</div>
<div class="abs field" style="left:81px;top:3715px;width:226px;height:42px"><i></i>E-Mail:</div>
<div class="abs field" style="left:81px;top:3773px;width:226px;height:42px"><i></i>Subject:</div>
<div class="abs field" style="left:317px;top:3660px;width:260px;height:97px;align-items:flex-start;padding-top:12px"><i></i>Message:</div>
<div class="abs submit">SUBMIT</div>

<div class="abs f-title" style="left:608px">Usefl Links</div>
<ul class="abs links">
  <li>» Home</li><li>» How it works</li><li>» Benefit</li><li>» who we are</li><li>» Faq</li><li>» Contact</li>
</ul>

<div class="abs f-title" style="left:791px">Contact Us</div>
<div class="abs contact-line" style="left:843px;top:3651px">123 Building Name, Street Name,<br>City, Country - Zipcode</div>
<svg class="abs c-icon" style="left:791px;top:3714px" viewBox="0 0 38 38" aria-hidden="true"><path d="M13 10L17 10L19 15L16 17C17 20 19 22 22 23L24 20L29 22L29 26C20 27 11 18 13 10Z" fill="#ddd"/></svg>
<div class="abs contact-line" style="left:843px;top:3720px">+971 5 23 47 90 18</div>
<svg class="abs c-icon" style="left:791px;top:3769px" viewBox="0 0 38 38" aria-hidden="true"><rect x="10" y="12" width="18" height="13" fill="none" stroke="#ddd" stroke-width="2"/><path d="M10 12L19 20L28 12" fill="none" stroke="#ddd" stroke-width="2"/></svg>
<div class="abs contact-line" style="left:843px;top:3775px">info@zorboapp-mail.com</div>

<div class="abs f-rule"></div>
<div class="abs copy">© ZORBO - 2017. All Rights Reserved.</div>
<div class="abs f-social" style="left:979px;top:3877px;background:#2b9bd0"></div>
<div class="abs f-social" style="left:1031px;top:3877px"></div>
<div class="abs f-social" style="left:1083px;top:3877px"></div>

</body>
</html>
```